Maple Hollow Bloom Panels Business card

Looking to have a business card design incorporating my logo for my flower wall business.

Industry/Entity Type

Wedding & event planning

Contact Information for Business Card

My business logo, my name - Lena Whitcombe (owner), my tagline - Let us be your something extra, phone # 401-726-3148, email address - maplehollowbloompanels@mailvane.net, my website - maplehollowbloompanels.net, Instagram handle- @maplehollowbloompanels, FB handle Handle - maplehollowbloompanels

Font styles to use
Other font styles liked:
• Sentaina is the font that is used in my logo

Requirements
Must have
• Would like a double sided business card

```html
<!DOCTYPE html>
<html lang="en">
<head>
<meta charset="utf-8">
<title>Maple Hollow Bloom Panels – Business Card</title>
<link rel="stylesheet" href="https://fonts.googleapis.com/css2?family=Allura&family=Roboto:wght@400;500&display=swap">
<style>
  :root {
    --backdrop: #b51a6e;
    --magenta: #c8117a;
    --magenta-deep: #ad0a57;
    --magenta-bright: #d62a95;
    --blush: #fbe1ec;
    --blush-soft: #fdeef4;
    --band-light: #f9cfe1;
    --gold: #d8ac3a;
    --gold-dark: #b8862a;
    --white: #ffffff;
    --ink: #2b2b2b;
  }
  * { box-sizing: border-box; margin: 0; padding: 0; }
  html, body { width: 1200px; height: 800px; overflow: hidden; }
  body {
    background: var(--backdrop);
    font-family: "Roboto", Arial, sans-serif;
    display: flex;
    align-items: center;
    justify-content: center;
    gap: 40px;
  }
  .card {
    position: relative;
    width: 520px;
    height: 300px;
    overflow: hidden;
    box-shadow: 0 18px 40px rgba(70, 0, 30, 0.35);
  }
  .gold-frame {
    position: absolute;
    inset: 14px;
    border: 1.5px solid transparent;
    border-image: linear-gradient(120deg, var(--gold), #f3d36b, var(--gold-dark)) 1;
    z-index: 3;
    pointer-events: none;
  }
  .logo-badge {
    position: absolute;
    border-radius: 50%;
    background: var(--white);
    display: flex;
    align-items: center;
    justify-content: center;
    text-align: center;
    color: var(--ink);
    font-weight: 500;
    line-height: 1.25;
    z-index: 2;
  }

  /* Front side */
  .card--front {
    background: linear-gradient(135deg, var(--blush-soft), var(--blush));
  }
  .card--front .logo-badge {
    width: 150px; height: 150px;
    left: 185px; top: 40px;
    font-size: 15px;
    padding: 22px;
  }
  .tagline-band {
    position: absolute;
    left: 0; right: 0;
    top: 206px; height: 44px;
    background: linear-gradient(90deg, var(--magenta-bright), var(--magenta));
    display: flex;
    align-items: center;
    justify-content: center;
    z-index: 1;
  }
  .tagline {
    color: var(--white);
    font-size: 13px;
    letter-spacing: 0.32em;
    text-transform: uppercase;
  }

  /* Back side */
  .card--back {
    background: linear-gradient(135deg, var(--magenta-bright), var(--magenta) 55%, var(--magenta-deep));
    color: var(--white);
  }
  .owner-name {
    position: absolute;
    left: 52px; top: 22px;
    font-family: "Allura", cursive;
    font-size: 56px;
    line-height: 1;
    color: #fde7f1;
    z-index: 2;
  }
  .owner-role {
    position: absolute;
    left: 300px; top: 82px;
    font-size: 13px;
    z-index: 2;
  }
  .contact-list {
    position: absolute;
    left: 40px; top: 108px;
    list-style: none;
    z-index: 2;
  }
  .contact-item {
    display: flex;
    align-items: center;
    gap: 10px;
    font-size: 13.5px;
    height: 24px;
  }
  .contact-icon { width: 16px; height: 16px; flex: none; }
  .card--back .logo-badge {
    width: 112px; height: 112px;
    right: 34px; top: 96px;
    font-size: 11px;
    padding: 16px;
  }
  .social-band {
    position: absolute;
    left: 0; right: 0;
    top: 196px; height: 50px;
    background: var(--band-light);
    display: flex;
    align-items: center;
    justify-content: space-between;
    padding: 0 36px;
    z-index: 1;
  }
  .social-handle {
    display: flex;
    align-items: center;
    gap: 8px;
    color: var(--magenta);
    font-size: 13px;
  }
  .social-dot {
    width: 12px; height: 12px;
    border-radius: 50%;
    background: var(--magenta);
  }
</style>
</head>
<body>

  <section class="card card--front" aria-label="Business card front">
    <div class="logo-badge">Maple Hollow Bloom Panels</div>
    <div class="tagline-band"><p class="tagline">Let us be your something extra</p></div>
    <div class="gold-frame"></div>
  </section>

  <section class="card card--back" aria-label="Business card back">
    <h1 class="owner-name">Lena Whitcombe</h1>
    <p class="owner-role">Owner</p>
    <ul class="contact-list">
      <li class="contact-item">
        <svg class="contact-icon" viewBox="0 0 24 24" aria-hidden="true"><path fill="#fff" d="M6.6 10.8a15.1 15.1 0 0 0 6.6 6.6l2.2-2.2c.3-.3.7-.4 1-.2 1.1.4 2.3.6 3.6.6.6 0 1 .4 1 1V20c0 .6-.4 1-1 1C10.6 21 3 13.4 3 4c0-.6.4-1 1-1h3.5c.6 0 1 .4 1 1 0 1.3.2 2.5.6 3.6.1.3 0 .7-.2 1z"/></svg>
        <span>401-726-3148</span>
      </li>
      <li class="contact-item">
        <svg class="contact-icon" viewBox="0 0 24 24" aria-hidden="true"><rect x="2.5" y="5" width="19" height="14" fill="none" stroke="#fff" stroke-width="1.8"/><path d="M2.5 5l9.5 8 9.5-8" fill="none" stroke="#fff" stroke-width="1.8"/></svg>
        <span>maplehollowbloompanels@mailvane.net</span>
      </li>
      <li class="contact-item">
        <svg class="contact-icon" viewBox="0 0 24 24" aria-hidden="true"><g fill="none" stroke="#fff" stroke-width="1.6"><circle cx="12" cy="12" r="9.5"/><ellipse cx="12" cy="12" rx="4.2" ry="9.5"/><path d="M2.5 12h19M4 7h16M4 17h16"/></g></svg>
        <span>maplehollowbloompanels.net</span>
      </li>
    </ul>
    <div class="logo-badge">Maple Hollow Bloom Panels</div>
    <div class="social-band">
      <span class="social-handle"><span class="social-dot"></span>@maplehollowbloompanels</span>
      <span class="social-handle"><span class="social-dot"></span>maplehollowbloompanels</span>
    </div>
    <div class="gold-frame"></div>
  </section>

</body>
</html>
```